Website for Community Storage Startup Company

We're looking for a great design that looks good on mobile devices (as well as the web) - Layout should be responsive and able to scale to many sized devices.

It should provide a good user-experience for people browsing the site with heavy focus on search and search results pages - It should be extremely easy to search, see results and add your own information.

Search parameters should be Location (Text), Dates (Calendar pop up), Price (slider) with optional extra parameters to be displayed (You can just call them Parameter1, Parameter2 etc. for Examples- we'd like to see options of no extra parameters and up to 4 others)

Please include a favicon for the site - we've provided the logo we had designed.

Pages We Must Have:

1) Home Page
2) Search Page (most likely map based)
3) Search Results Page (most likely map based) - we want the search options/results to slide in and out as appropriate - please visualize
Information Page - this is branded and would present information for many possible pages like Terms & Conditions or a FAQ page etc.
4) My Account Page - Should be an inline editable page with Name/Address/Financial information etc. showing
5) Sign-up Page - This could be a slide in element on another page or part of the account page, or separate as you think works best

Ideally this would all work like a single page app with a common theme but we're interested to see your ideas of tying pages together or keeping them separate while fitting our brief.

Examples of things we like;

a) roomvale - mobile and web based layouts - we like the map on the side and data input on the other side
b) http://www.qorvent.example/qv/airlines/ - scroll down slightly to the first video - about 0:28 in we like the map on the side and the panel on the side with details you can refine etc. All over we like the site presented through the video

Nice to Have:
- The ability to provide the finished design as sliced CSS, HTML and JS
Updates

Project Deadline Extended
Reason: Feedback has suggested that the timeline is too tight, we've extended it but are very interested in seeing initial page designs sooner rather than later to provide feedback. Thanks!

Thanks for your contributions so far :)  We've come to realize that in general we're preferring darker color schemes - if you're pulling colors from our logo try to stick to the text colors :)

We like narrow headers and footers and a map based interface. Sliders for information are good and we'd like to see how checkbox elements would play out too.

Examples of how information may pop up from markers would be nice too.

Thanks for everything so far!

Target Market(s)

Young to middle aged adults in the USA

Industry/Entity Type

Airlines

Font styles to use
Sans Serif

Colors

Designer to choose colors to be used in the design.

Requirements
Must have
• 1) Home Page
Nice to have
• The ability to provide the finished design as sliced CSS, HTML and JS

We think a map with markers should figure heavily in search results and searching.

```html
<!DOCTYPE html>
<html lang="en">
<head>
<meta charset="utf-8">
<title>Cratewell – My Account</title>
<link href="https://fonts.googleapis.com/css2?family=Roboto+Condensed:wght@300;400;700&family=Roboto:wght@300;400;500;700&display=swap" rel="stylesheet">
<style>
  :root {
    --bg: #252525;
    --header-bg: #2b2828;
    --accent: #45c4d3;
    --text: #ffffff;
    --text-soft: #e6e6e6;
    --rule: #6b6b6b;
    --frame: #9a9a9a;
    --track: #2f2f2f;
    --thumb: #6e6e6e;
  }
  * { box-sizing: border-box; margin: 0; padding: 0; }
  html, body { width: 685px; height: 1200px; overflow: hidden; background: var(--bg); }
  body { position: relative; font-family: "Roboto", sans-serif; color: var(--text); }
  .abs { position: absolute; }

  .site-header { left: 0; top: 0; width: 685px; height: 115px; background: var(--header-bg); }
  .brand { left: 65px; top: 40px; font-family: "Roboto", sans-serif; font-weight: 300; font-size: 48px; letter-spacing: 2px; color: var(--text); line-height: 1; }
  .log-off { left: 518px; top: 83px; display: flex; align-items: center; gap: 6px; font-family: "Roboto Condensed", sans-serif; font-size: 14px; color: var(--text); }
  .header-rule { left: 65px; top: 113px; width: 536px; height: 2px; background: var(--accent); }

  .account-tab { left: 65px; top: 124px; width: 534px; height: 63px; border: 1px solid var(--frame); display: flex; align-items: center; justify-content: center; font-size: 19px; color: var(--accent); letter-spacing: .3px; }

  .account-row { left: 69px; width: 533px; display: flex; align-items: center; border-bottom: 1px solid var(--rule); font-size: 24px; font-weight: 300; }
  .account-row .icon { width: 81px; display: flex; justify-content: center; }

  .info-text { left: 104px; top: 414px; width: 436px; font-family: "Roboto Condensed", sans-serif; font-weight: 300; font-size: 16px; letter-spacing: -0.15px; line-height: 23.7px; text-align: justify; color: var(--text-soft); }
  .scroll-track { left: 578px; top: 421px; width: 13px; height: 134px; border: 1px solid #555; background: var(--track); }
  .scroll-thumb { left: 580px; top: 462px; width: 9px; height: 40px; background: var(--thumb); }
  .btn-more { left: 104px; top: 578px; width: 156px; height: 29px; background: var(--accent); border-radius: 3px; font-size: 13px; display: flex; align-items: center; justify-content: center; color: var(--text); }

  .rule { left: 69px; width: 533px; height: 1px; background: var(--rule); }

  .signin-title { left: 71px; top: 846px; font-size: 19px; font-weight: 400; letter-spacing: .2px; }
  .signin-title strong { font-weight: 700; }
  .field { top: 898px; width: 256px; height: 52px; border: 1px solid var(--frame); padding-left: 29px; display: flex; align-items: center; font-size: 16px; color: var(--text-soft); }
  .btn-login { left: 66px; top: 973px; width: 255px; height: 47px; background: var(--accent); font-size: 19px; display: flex; align-items: center; justify-content: center; color: var(--text); }
  .forgot { left: 70px; top: 1067px; font-size: 13px; color: var(--text); }
</style>
</head>
<body>
  <header class="site-header abs"></header>
  <div class="brand abs">Cratewell</div>
  <div class="log-off abs">
    <svg width="20" height="17" viewBox="0 0 20 17" aria-hidden="true">
      <path d="M8 1H2v15h6" fill="none" stroke="#fff" stroke-width="2.4"/>
      <path d="M7 6h6V2l6 6.5-6 6.5v-4H7z" fill="#fff"/>
    </svg>
    <span>LOG OFF</span>
  </div>
  <div class="header-rule abs"></div>

  <div class="account-tab abs">MY ACCOUNT</div>

  <div class="account-row abs" style="top:208px;height:60px;">
    <span class="icon">
      <svg width="28" height="36" viewBox="0 0 28 36" aria-hidden="true">
        <circle cx="14" cy="9" r="8" fill="#fff"/>
        <path d="M1 35c0-10 4-16 13-16s13 6 13 16z" fill="#fff"/>
      </svg>
    </span>
    <span>Name</span>
  </div>
  <div class="account-row abs" style="top:268px;height:65px;">
    <span class="icon">
      <svg width="34" height="30" viewBox="0 0 34 30" aria-hidden="true">
        <path d="M17 1L1 15h5v14h8v-9h6v9h8V15h5z" fill="#fff"/>
      </svg>
    </span>
    <span>Address</span>
  </div>
  <div class="account-row abs" style="top:333px;height:60px;">
    <span class="icon">
      <svg width="20" height="36" viewBox="0 0 20 36" aria-hidden="true">
        <circle cx="13" cy="5" r="4.2" fill="#fff"/>
        <path d="M5 14h10l-5 17h5l-1 3H2l5-17H4z" fill="#fff"/>
      </svg>
    </span>
    <span>Financial information</span>
  </div>

  <p class="info-text abs">It has survived not only five centuries, but also the leap into electronic typesetting, remaining essentially unchanged. It was popularised in the 1960s with the release of Typestack sheets containing Lorem Ipsum passages, and more recently with desktop publishing software like Quillsoft PageSetter including versions of Lorem Ipsum.</p>
  <div class="scroll-track abs"></div>
  <div class="scroll-thumb abs"></div>
  <div class="btn-more abs">MORE INFORMATION</div>

  <div class="rule abs" style="top:639px;"></div>
  <div class="account-row abs" style="top:640px;height:70px;">
    <span class="icon">
      <svg width="42" height="26" viewBox="0 0 42 26" aria-hidden="true">
        <path d="M1 2l20 22L41 2" fill="none" stroke="#fff" stroke-width="2"/>
      </svg>
    </span>
    <span>History of my search</span>
  </div>

  <h2 class="signin-title abs"><strong>SIGN INTO</strong> YOUR ACCOUNT</h2>
  <div class="field abs" style="left:65px;">Name</div>
  <div class="field abs" style="left:345px;">Password</div>
  <div class="btn-login abs">LOG IN</div>
  <div class="rule abs" style="top:1046px;"></div>
  <div class="forgot abs">FORGOT YOUR PASSWORD?</div>
</body>
</html>
```